Stationary Design for Energy Trading & Supply Company
Business Cards, Stationary, PowerPoint template, word template for letters and documentations
Creative Brief
Professional
Martin Keslowe
Executive Director
Suite 18B, Floor 41, Corvana Business Tower (Corvana Tower North) Halden Parkway Road, Market Quarter 5 Dubai, United Arab Emirates
m@q.example
www.tribeca-volt.example
email is martin.keslowe@tribeca-volt.example
just the icon with website below www.tribeca-volt.example

```html
<!DOCTYPE html>
<html lang="en">
<head>
<meta charset="utf-8">
<title>Tribeca Volt – Business Card</title>
<link href="https://fonts.googleapis.com/css2?family=Montserrat:wght@700;800&family=Roboto:wght@400;500;700&display=swap" rel="stylesheet">
<style>
  :root {
    --bg: #e7e9ec;
    --navy: #14264a;
    --navy-deep: #0c1a36;
    --teal: #2a7f8c;
    --ink: #3a3f47;
    --paper: #ffffff;
  }
  * { box-sizing: border-box; margin: 0; padding: 0; }
  html, body { width: 1200px; height: 706px; overflow: hidden; }
  body {
    background: var(--bg);
    font-family: "Roboto", Arial, sans-serif;
    display: flex;
    align-items: center;
    justify-content: center;
    gap: 60px;
  }
  .card {
    width: 520px;
    height: 300px;
    border-radius: 14px;
    position: relative;
    overflow: hidden;
    box-shadow: 0 10px 30px rgba(0,0,0,.18);
  }
  .card-front {
    background: linear-gradient(135deg, #1d3566 0%, var(--navy) 55%, var(--navy-deep) 100%);
    display: flex;
    align-items: center;
    justify-content: center;
  }
  .wordmark {
    display: flex;
    align-items: center;
    gap: 12px;
    font-family: "Montserrat", Arial, sans-serif;
    font-weight: 800;
    letter-spacing: 2px;
    text-transform: uppercase;
  }
  .wordmark .dot { border-radius: 50%; flex: none; }
  .card-front .wordmark { font-size: 40px; color: #2c4a82; }
  .card-front .wordmark .dot { width: 30px; height: 30px; background: #2c4a82; }

  .card-back { background: var(--paper); }
  .card-back .wordmark {
    position: absolute; left: 26px; top: 34px;
    font-size: 20px; color: var(--navy); gap: 8px;
  }
  .card-back .wordmark .dot { width: 18px; height: 18px; background: var(--navy); }
  .accent-disc {
    position: absolute; right: -40px; top: -30px;
    width: 250px; height: 250px; border-radius: 50%;
    background: linear-gradient(160deg, var(--navy) 0%, #1f4d6b 60%, var(--teal) 100%);
  }
  .identity {
    position: absolute; left: 26px; top: 112px;
    border-left: 6px solid var(--teal);
    padding-left: 10px;
  }
  .identity .name { font-size: 22px; font-weight: 700; color: var(--navy); line-height: 1.1; }
  .identity .role { font-size: 10px; color: var(--teal); margin-top: 2px; }
  .address {
    position: absolute; left: 42px; top: 160px; width: 230px;
    font-size: 8.5px; line-height: 1.45; color: var(--ink);
  }
  .contacts {
    position: absolute; left: 42px; top: 226px;
    list-style: none; font-size: 8.5px; color: var(--ink);
  }
  .contacts li { display: flex; align-items: center; gap: 7px; margin-bottom: 5px; }
  .contacts svg { width: 11px; height: 11px; fill: var(--navy); flex: none; }
</style>
</head>
<body>
  <section class="card card-front" aria-label="Card front">
    <div class="wordmark"><span class="dot"></span>Tribeca Volt</div>
  </section>

  <section class="card card-back" aria-label="Card back">
    <div class="accent-disc"></div>
    <div class="wordmark"><span class="dot"></span>Tribeca Volt</div>

    <div class="identity">
      <p class="name">Martin Keslowe</p>
      <p class="role">Executive Director</p>
    </div>

    <p class="address">
      Suite 18B, Floor 41,<br>
      Corvana Business Tower (Corvana Tower North)<br>
      Halden Parkway Road, Market Quarter 5<br>
      Dubai, United Arab Emirates
    </p>

    <ul class="contacts">
      <li>
        <svg viewBox="0 0 24 24"><path d="M6.6 10.8a15.1 15.1 0 0 0 6.6 6.6l2.2-2.2c.3-.3.7-.4 1-.2 1.1.4 2.3.6 3.6.6.6 0 1 .4 1 1V20c0 .6-.4 1-1 1A17 17 0 0 1 3 4c0-.6.4-1 1-1h3.5c.6 0 1 .4 1 1 0 1.3.2 2.5.6 3.6.1.3 0 .7-.2 1z"/></svg>
        +971 50 555 0148
      </li>
      <li>
        <svg viewBox="0 0 24 24"><path d="M3 5h18v14H3z M3 5l9 7 9-7" fill="none" stroke="#14264a" stroke-width="2"/></svg>
        martin.keslowe@tribeca-volt.example
      </li>
      <li>
        <svg viewBox="0 0 24 24"><circle cx="12" cy="12" r="9" fill="none" stroke="#14264a" stroke-width="2"/><path d="M3 12h18M12 3c3 3 3 15 0 18M12 3c-3 3-3 15 0 18" fill="none" stroke="#14264a" stroke-width="1.6"/></svg>
        www.tribeca-volt.example
      </li>
    </ul>
  </section>
</body>
</html>
```